Electronic Time-sheet & Training Tracker for Mobile phone

App should have two functions:Access by Quillon and Vextora:Employee Tracker: I need to be able to add/edit employees and personal information (example: address, DL number, SS number, DOB, employee number), drug screen information (type DCCHA and expiration date, DCCFO and expiration date, DCCHT and expiration date, PRAV Background and expiration date) and enter multiple training records (KEMB8 and expiration date). It would be great to receive an expiration alert.The employee would only have visibility to his own. Supervisors would have overall visibility.Time-Sheet:I need a time-sheet that can be accessed on the phone, be completed, then have the ability to electronically sign and submitted. The timesheet needs to be used two-fold for supervision to verify hours and edit (if need be), he would approve and forward to payroll. The time-sheet should be daily or weekly if we can get the data to fit. We are trying to streamline field supervisors having to log on to a computer to access a server just to do time-sheets. We need it to be user-friendly. We need to have two places to have electronic signatures (employee and supervisor).
A couple of designers have asked for an additional day. Others are making changes based on feedback.
Industrial (Oil ad Gas)
- Timesheet portion may require multiple entries with billable, non-billable, shop drop-down and job number and category code (LRS, HTS, FMS, ITP, OBS, HTT, NDE)
- Tracker - Training expiration alert or notifications by email to employee and supervisors.

```html
<!DOCTYPE html>
<html lang="en">
<head>
<meta charset="utf-8">
<title>Haldrik Timesheet – Approval Flow</title>
<link href="https://fonts.googleapis.com/css2?family=Oswald:wght@400;500;700&family=Open+Sans:wght@400;600;700&family=Tinos&display=swap" rel="stylesheet">
<style>
:root{
  --bg:#8a8a8a;
  --paper:#ffffff;
  --ink:#1f1f1f;
  --muted:#6b6b6b;
  --rule:#d9d9d9;
  --orange:#cc5a1a;
  --peach:#fbe9e0;
  --band:#efefef;
  --sig:#ececec;
}
*{box-sizing:border-box;margin:0;padding:0}
html,body{width:1200px;height:949px;overflow:hidden;background:var(--bg)}
body{position:relative;font-family:"Open Sans",sans-serif;color:var(--ink)}
.step-title{position:absolute;top:80px;width:300px;text-align:center;font-family:"Tinos",serif;font-size:12.5px;color:#fff}
.step-title small{font-size:9.5px;letter-spacing:.3px}
.screen{position:absolute;top:116px;width:256px;background:var(--paper);border-radius:22px;overflow:hidden}
.abs{position:absolute}
.status{top:11px;left:22px;right:20px;font-size:7px;color:#aaa;display:flex;justify-content:space-between}
.status i{display:inline-block;width:8px;height:4px;background:#ccc;margin-left:3px;border-radius:1px}
.back{top:40px;left:11px;font-family:"Oswald",sans-serif;font-size:7px;color:var(--ink)}
.brand{top:58px;width:100%;text-align:center;font-family:"Oswald",sans-serif;font-weight:700;font-size:20px;letter-spacing:2px;color:var(--ink)}
.sheet-title{top:89px;width:100%;display:flex;align-items:center;font-family:"Oswald",sans-serif;font-weight:500;font-size:11.5px;letter-spacing:.3px}
.sheet-title::before,.sheet-title::after{content:"";flex:1;height:1.5px;background:var(--ink)}
.sheet-title span{padding:0 6px}
.meta{left:11px;display:flex;align-items:center}
.meta .ic{width:27px;height:27px;border-radius:50%;background:var(--ink);display:flex;align-items:center;justify-content:center;margin-right:6px}
.meta .lbl{font-size:6.5px;font-weight:700;color:var(--orange);letter-spacing:.3px}
.meta .val{font-size:11px;font-weight:600;line-height:1.2}
.meta .val em{font-style:normal;font-weight:400;font-size:8px}
.thead,.row{left:0;right:0;display:grid;grid-template-columns:11px 84px 44px 38px 38px 36px 1fr;align-items:center;font-family:"Oswald",sans-serif}
.thead{top:264px;height:15px;font-size:6.5px;color:#888;border-bottom:1.5px solid var(--ink)}
.row{height:39px;font-size:8px;border-bottom:1px solid var(--rule)}
.row:last-of-type{border-bottom:1.5px solid var(--ink)}
.row>*:nth-child(n+3),.thead>*:nth-child(n+3){text-align:center}
.row.changed{background:var(--peach)}
.row .zero{color:var(--orange)}
.row.swiped{grid-template-columns:0 78px 44px 38px 38px 38px 1fr}
.row.swiped .shop{overflow:hidden;white-space:nowrap;direction:rtl;text-align:left}
.trash{height:100%;background:var(--peach);display:flex;align-items:center;justify-content:center}
.total{left:0;right:0;height:28px;background:var(--band);display:flex;align-items:center;justify-content:flex-end;padding-right:18px;font-family:"Oswald",sans-serif;font-size:8px}
.total b{font-weight:500;margin-left:18px}
.total.changed{background:var(--peach)}
.total.changed b{color:var(--orange)}
.add{left:11px;width:82px;height:20px;border:1px solid var(--orange);border-radius:10px;color:var(--orange);font-size:6.5px;font-weight:700;display:flex;align-items:center;justify-content:center}
.sig-label{left:11px;font-size:8px;font-weight:600;letter-spacing:.2px}
.sig{left:11px;right:11px;height:38px;border:1px solid #999;border-left:4px solid var(--ink);display:flex}
.sig .mark{flex:1;margin:8px 10px;background:var(--sig);border-radius:3px}
.sig .date{width:38px;border-left:1px solid #999;margin:6px 0;font-family:"Oswald",sans-serif;font-size:7px;text-align:center;line-height:1.25;padding-top:3px}
.sig .date small{font-size:6px}
.btn{left:46px;width:164px;height:32px;border-radius:3px;color:#fff;font-family:"Oswald",sans-serif;font-weight:500;font-size:12px;display:flex;align-items:center;justify-content:center;gap:5px;background:var(--orange)}
.btn.dark{background:var(--ink)}
.home-bar{left:83px;width:90px;height:3px;border-radius:2px;background:#e5e5e5}
.tip{top:398px;left:210px;width:38px;height:36px;background:var(--ink);color:#fff;border-radius:3px;font-family:"Oswald",sans-serif;text-align:center;font-size:8px;padding-top:4px;line-height:1.5}
.tip small{display:block;font-size:6.5px;border-bottom:1px solid #fff;margin:0 6px 2px}
.tip::after{content:"";position:absolute;left:15px;bottom:-5px;border:4px solid transparent;border-top-color:var(--ink);border-bottom:0}
.note{position:absolute;width:260px;text-align:center;font-family:"Tinos",serif;font-size:12.5px;line-height:17.6px;color:#fff}
.note p+p{margin-top:18px}
</style>
</head>
<body>

<div class="step-title" style="left:22px"><small>STEP</small> 4: SUPERVISOR reviews.</div>
<div class="step-title" style="left:310px"><small>STEP</small> 5: SUPERVISOR modifies.</div>
<div class="step-title" style="left:598px"><small>STEP</small> 6: EMPLOYEE reviews &amp; re-signs.</div>
<div class="step-title" style="left:886px"><small>STEP</small> 7: SUPERVISOR signs &amp; submits.</div>

<!-- Step 4 -->
<section class="screen" style="left:40px;height:722px">
  <div class="abs status"><span>5:30</span><span><i></i><i></i><i></i></span></div>
  <div class="abs back">&#8249;&nbsp; BACK</div>
  <div class="abs brand">HALDRIK</div>
  <div class="abs sheet-title"><span>TIMESHEET</span></div>
  <div class="abs meta" style="top:128px"><div class="ic"><svg width="12" height="12" viewBox="0 0 12 12"><circle cx="6" cy="3.5" r="2.6" fill="#fff"/><path d="M1 12c0-3 2.3-5 5-5s5 2 5 5z" fill="#fff"/></svg></div><div><div class="lbl">EMPLOYEE</div><div class="val">John Doe <em>(Employee#)</em></div></div></div>
  <div class="abs meta" style="top:167px"><div class="ic"><svg width="14" height="10" viewBox="0 0 14 10"><path d="M1 5c2-3.5 10-3.5 12 0c-2 3.5-10 3.5-12 0z" fill="#fff"/><circle cx="7" cy="5" r="2" fill="#1f1f1f"/></svg></div><div><div class="lbl">SUPERVISOR</div><div class="val">Jason Doe <em>(Employee#)</em></div></div></div>
  <div class="abs meta" style="top:205px"><div class="ic"><svg width="12" height="12" viewBox="0 0 12 12"><rect x="1" y="2" width="10" height="9" rx="1" fill="none" stroke="#fff" stroke-width="1.3"/><path d="M1 4.5h10M3.5 1v2M8.5 1v2" stroke="#fff" stroke-width="1.3"/></svg></div><div><div class="lbl">DATE</div><div class="val">February 5, 2019</div></div></div>
  <div class="abs thead"><span></span><span>SHOP</span><span>JOB #</span><span>CATEGORY</span><span>BILLABLE</span><span>HOURS</span></div>
  <div class="abs row" style="top:280px"><span></span><span>Shop Name 1</span><span>123456</span><span>LRS</span><span>&#10004;</span><span>5</span></div>
  <div class="abs row swiped" style="top:319px"><span></span><span class="shop">Shop Name 2</span><span>234567</span><span>HTS</span><span>&#10004;</span><span>1</span><span class="trash"><svg width="8" height="9" viewBox="0 0 8 9"><path d="M0 1.5h8M3 0h2M1 2.5l.6 6h4.8l.6-6" fill="none" stroke="#cc5a1a" stroke-width="1.1"/></svg></span></div>
  <div class="abs row" style="top:358px"><span></span><span>Shop Name 3</span><span>345678</span><span>FMS</span><span></span><span>1</span></div>
  <div class="abs row" style="top:397px"><span></span><span>Shop Name 4</span><span>456789</span><span>NDE</span><span>&#10004;</span><span>1</span></div>
  <div class="abs total" style="top:436px">TOTAL: <b>8 hrs</b></div>
  <div class="abs add" style="top:470px">+ ADD PHASE</div>
  <div class="abs sig-label" style="top:522px">EMPLOYEE SIGNATURE</div>
  <div class="abs sig" style="top:536px"><div class="mark" role="img" aria-label="Handwritten signature of John Doe"></div><div class="date">FEB. 5<br><small>2019</small></div></div>
  <div class="abs sig-label" style="top:589px">SUPERVISOR SIGNATURE</div>
  <div class="abs sig" style="top:603px;border-color:#999"></div>
  <div class="abs btn" style="top:658px">&#10148; SUBMIT</div>
  <div class="abs home-bar" style="top:712px"></div>
</section>

<!-- Step 5 -->
<section class="screen" style="left:328px;height:588px">
  <div class="abs status"><span>5:30</span><span><i></i><i></i><i></i></span></div>
  <div class="abs back">&#8249;&nbsp; BACK</div>
  <div class="abs brand">HALDRIK</div>
  <div class="abs sheet-title"><span>TIMESHEET</span></div>
  <div class="abs meta" style="top:128px"><div class="ic"><svg width="12" height="12" viewBox="0 0 12 12"><circle cx="6" cy="3.5" r="2.6" fill="#fff"/><path d="M1 12c0-3 2.3-5 5-5s5 2 5 5z" fill="#fff"/></svg></div><div><div class="lbl">EMPLOYEE</div><div class="val">John Doe <em>(Employee#)</em></div></div></div>
  <div class="abs meta" style="top:167px"><div class="ic"><svg width="14" height="10" viewBox="0 0 14 10"><path d="M1 5c2-3.5 10-3.5 12 0c-2 3.5-10 3.5-12 0z" fill="#fff"/><circle cx="7" cy="5" r="2" fill="#1f1f1f"/></svg></div><div><div class="lbl">SUPERVISOR</div><div class="val">Jason Doe <em>(Employee#)</em></div></div></div>
  <div class="abs meta" style="top:205px"><div class="ic"><svg width="12" height="12" viewBox="0 0 12 12"><rect x="1" y="2" width="10" height="9" rx="1" fill="none" stroke="#fff" stroke-width="1.3"/><path d="M1 4.5h10M3.5 1v2M8.5 1v2" stroke="#fff" stroke-width="1.3"/></svg></div><div><div class="lbl">DATE</div><div class="val">February 5, 2019</div></div></div>
  <div class="abs thead"><span></span><span>SHOP</span><span>JOB #</span><span>CATEGORY</span><span>BILLABLE</span><span>HOURS</span></div>
  <div class="abs row" style="top:280px"><span></span><span>Shop Name 1</span><span>123456</span><span>LRS</span><span>&#10004;</span><span>5</span></div>
  <div class="abs row changed" style="top:319px"><span></span><span>Shop Name 2</span><span>234567</span><span>HTS</span><span>&#10004;</span><span class="zero">0</span></div>
  <div class="abs row" style="top:358px"><span></span><span>Shop Name 3</span><span>345678</span><span>FMS</span><span></span><span>1</span></div>
  <div class="abs row" style="top:397px"><span></span><span>Shop Name 4</span><span>456789</span><span>NDE</span><span>&#10004;</span><span>1</span></div>
  <div class="abs total changed" style="top:436px">TOTAL: <b>7 hrs</b></div>
  <div class="abs add" style="top:470px">+ ADD PHASE</div>
  <div class="abs btn dark" style="top:524px">&#10148; RETURN TO EMPLOYEE</div>
  <div class="abs home-bar" style="top:580px"></div>
</section>
<div class="note" style="left:326px;top:724px">
  <p>When SUPERVISOR modifies, the phase will be highlighted. (When SUPERVISOR deleted the phase, it is still kept and the hour is marked as “0”)</p>
  <p>When any changes are made, the timesheet will be sent back to the employee for his/her review &amp; signature.</p>
</div>

<!-- Step 6 -->
<section class="screen" style="left:616px;height:628px">
  <div class="abs status"><span>5:30</span><span><i></i><i></i><i></i></span></div>
  <div class="abs brand">HALDRIK</div>
  <div class="abs sheet-title"><span>TIMESHEET</span></div>
  <div class="abs meta" style="top:128px"><div class="ic"><svg width="12" height="12" viewBox="0 0 12 12"><circle cx="6" cy="3.5" r="2.6" fill="#fff"/><path d="M1 12c0-3 2.3-5 5-5s5 2 5 5z" fill="#fff"/></svg></div><div><div class="lbl">EMPLOYEE</div><div class="val">John Doe <em>(Employee#)</em></div></div></div>
  <div class="abs meta" style="top:167px"><div class="ic"><svg width="14" height="10" viewBox="0 0 14 10"><path d="M1 5c2-3.5 10-3.5 12 0c-2 3.5-10 3.5-12 0z" fill="#fff"/><circle cx="7" cy="5" r="2" fill="#1f1f1f"/></svg></div><div><div class="lbl">SUPERVISOR</div><div class="val">Jason Doe <em>(Employee#)</em></div></div></div>
  <div class="abs meta" style="top:205px"><div class="ic"><svg width="12" height="12" viewBox="0 0 12 12"><rect x="1" y="2" width="10" height="9" rx="1" fill="none" stroke="#fff" stroke-width="1.3"/><path d="M1 4.5h10M3.5 1v2M8.5 1v2" stroke="#fff" stroke-width="1.3"/></svg></div><div><div class="lbl">DATE</div><div class="val">February 5, 2019</div></div></div>
  <div class="abs thead"><span></span><span>SHOP</span><span>JOB #</span><span>CATEGORY</span><span>BILLABLE</span><span>HOURS</span></div>
  <div class="abs row" style="top:280px"><span></span><span>Shop Name 1</span><span>123456</span><span>LRS</span><span>&#10004;</span><span>5</span></div>
  <div class="abs row changed" style="top:319px"><span></span><span>Shop Name 2</span><span>234567</span><span>HTS</span><span>&#10004;</span><span class="zero">0</span></div>
  <div class="abs row" style="top:358px"><span></span><span>Shop Name 3</span><span>345678</span><span>FMS</span><span></span><span>1</span></div>
  <div class="abs row" style="top:397px"><span></span><span>Shop Name 4</span><span>456789</span><span>NDE</span><span>&#10004;</span><span>1</span></div>
  <div class="abs total changed" style="top:436px">TOTAL: <b>7 hrs</b></div>
  <div class="abs tip"><small>It was</small>8 hrs</div>
  <div class="abs sig-label" style="top:495px">EMPLOYEE SIGNATURE</div>
  <div class="abs sig" style="top:509px"><div class="mark" role="img" aria-label="Handwritten signature of John Doe"></div><div class="date">FEB. 6<br><small>2019</small></div></div>
  <div class="abs btn" style="top:564px">&#10148; SEND TO SUPERVISOR</div>
  <div class="abs home-bar" style="top:620px"></div>
</section>
<div class="note" style="left:614px;top:764px">
  <p>EMPLOYEE cannot modify info. on this screen. He/she can only sign.</p>
  <p>EMPLOYEE taps on the highlighted info, he/she can review the original info. in the tooltip.</p>
</div>

<!-- Step 7 -->
<section class="screen" style="left:904px;height:684px">
  <div class="abs status"><span>5:30</span><span><i></i><i></i><i></i></span></div>
  <div class="abs brand">HALDRIK</div>
  <div class="abs sheet-title"><span>TIMESHEET</span></div>
  <div class="abs meta" style="top:128px"><div class="ic"><svg width="12" height="12" viewBox="0 0 12 12"><circle cx="6" cy="3.5" r="2.6" fill="#fff"/><path d="M1 12c0-3 2.3-5 5-5s5 2 5 5z" fill="#fff"/></svg></div><div><div class="lbl">EMPLOYEE</div><div class="val">John Doe <em>(Employee#)</em></div></div></div>
  <div class="abs meta" style="top:167px"><div class="ic"><svg width="14" height="10" viewBox="0 0 14 10"><path d="M1 5c2-3.5 10-3.5 12 0c-2 3.5-10 3.5-12 0z" fill="#fff"/><circle cx="7" cy="5" r="2" fill="#1f1f1f"/></svg></div><div><div class="lbl">SUPERVISOR</div><div class="val">Jason Doe <em>(Employee#)</em></div></div></div>
  <div class="abs meta" style="top:205px"><div class="ic"><svg width="12" height="12" viewBox="0 0 12 12"><rect x="1" y="2" width="10" height="9" rx="1" fill="none" stroke="#fff" stroke-width="1.3"/><path d="M1 4.5h10M3.5 1v2M8.5 1v2" stroke="#fff" stroke-width="1.3"/></svg></div><div><div class="lbl">DATE</div><div class="val">February 5, 2019</div></div></div>
  <div class="abs thead"><span></span><span>SHOP</span><span>JOB #</span><span>CATEGORY</span><span>BILLABLE</span><span>HOURS</span></div>
  <div class="abs row" style="top:280px"><span></span><span>Shop Name 1</span><span>123456</span><span>LRS</span><span>&#10004;</span><span>5</span></div>
  <div class="abs row" style="top:319px"><span></span><span>Shop Name 3</span><span>345678</span><span>FMS</span><span></span><span>1</span></div>
  <div class="abs row" style="top:358px"><span></span><span>Shop Name 4</span><span>456789</span><span>NDE</span><span>&#10004;</span><span>1</span></div>
  <div class="abs total" style="top:397px">TOTAL: <b>7 hrs</b></div>
  <div class="abs add" style="top:431px">+ ADD PHASE</div>
  <div class="abs sig-label" style="top:483px">EMPLOYEE SIGNATURE</div>
  <div class="abs sig" style="top:498px"><div class="mark" role="img" aria-label="Handwritten signature of John Doe"></div><div class="date">FEB. 6<br><small>2019</small></div></div>
  <div class="abs sig-label" style="top:550px">SUPERVISOR SIGNATURE</div>
  <div class="abs sig" style="top:565px"><div class="mark" role="img" aria-label="Handwritten signature of Jason Doe"></div><div class="date">FEB. 6<br><small>2019</small></div></div>
  <div class="abs btn" style="top:619px">&#10148; SUBMIT</div>
  <div class="abs home-bar" style="top:675px"></div>
</section>

</body>
</html>
```